VORLEN Website Design

We need a website designed for our company VORLEN. We are a luxury lifestyle club that will provide benefits and services for our members. The site should be clean & sleek, preferably using black and white (or darker colors). (example sites: brimvale.example, tusko.example)

Here is a link of a sample page I did using wix. (https://pelmundry4.sitebuild.example/mypage) This can be used to get a general idea.

Target Market(s)

Upper Middle Class in the United States

Number of Pages Required

5+ page

Font styles to use
Sans Serif
Other font styles liked:
• Arial (or other similar fonts)

Requirements
Must have
• A clean design that is eye-catching and speaks to our company.
Nice to have
• Ideas for copy.

```html
<!DOCTYPE html>
<html lang="en">
<head>
<meta charset="utf-8">
<title>VORLEN – Members Only Lifestyle Club</title>
<link rel="stylesheet" href="https://fonts.googleapis.com/css2?family=Montserrat:wght@300;400;500;600;700&display=swap">
<style>
:root{
  --ink:#111111;
  --black:#000000;
  --white:#ffffff;
  --grey:#8a8a8a;
  --light:#f2f2f2;
  --line:#d6d6d6;
  --nav:#1c1c1c;
  --foot-bar:#3a3a3a;
  --accent:#d49a3a;
}
*{box-sizing:border-box;margin:0;padding:0}
html,body{width:1200px;height:4772px;overflow:hidden}
body{font-family:"Montserrat",Arial,sans-serif;color:var(--ink);background:var(--white);position:relative}
section,header,nav,footer{position:relative;width:1200px;overflow:hidden}
.abs{position:absolute}
.btn{position:absolute;display:flex;align-items:center;justify-content:center;font-size:13px;height:30px;color:var(--white);background:var(--black)}
.center{left:0;right:0;text-align:center}

/* header */
.site-header{height:128px;background:var(--white)}
.logo{left:84px;top:36px;font-size:50px;font-weight:300;letter-spacing:1px}
.contact-item{top:44px;text-align:center}
.contact-item small{display:block;font-size:13px;color:var(--grey)}
.contact-item strong{display:block;font-size:16px;font-weight:600;margin-top:2px}
.social{display:flex;gap:8px;margin-top:6px;justify-content:center}
.social i{width:14px;height:14px;border-radius:50%;background:var(--ink);display:block}

/* nav */
.main-nav{height:36px;background:var(--nav);color:var(--white);font-size:15px}
.main-nav .item{position:absolute;top:0;height:36px;line-height:36px}
.main-nav .home{left:130px;width:72px;text-align:center;background:#6b6b6b}
.search{position:absolute;left:860px;top:7px;width:240px;height:22px;background:var(--white);color:var(--grey);font-size:12px;line-height:22px;padding-left:8px}

/* hero */
.hero{height:636px;background:linear-gradient(100deg,#5b3420 0%,#a5714a 35%,#3b2418 62%,#1d140f 80%,#6a5436 100%)}
.hero h1{left:130px;width:520px;top:226px;text-align:center;font-size:26px;font-weight:500;color:var(--white);white-space:nowrap;line-height:32px}
.hero p{left:160px;width:460px;top:276px;text-align:center;font-size:12px;line-height:18px;color:#e8e8e8}
.hero .btn{top:352px;background:rgba(0,0,0,.75);font-size:12px}
.dots{left:574px;top:576px;display:flex;gap:10px}
.dots i{width:9px;height:9px;border-radius:50%;background:rgba(255,255,255,.5);display:block}
.dots i:first-child{background:var(--white)}

/* about */
.about{height:560px}
.about h2{left:84px;top:148px;font-size:28px;font-weight:400}
.about h2 b{font-weight:700}
.about h3{left:84px;top:228px;font-size:14px;font-weight:600}
.about p{left:84px;top:262px;width:720px;font-size:12px;line-height:18px;color:#666}
.about-photo{left:820px;top:92px;width:292px;height:372px;background:linear-gradient(160deg,#b9c4cf,#5e6a78 55%,#2a2f38)}

/* we are */
.we-are{height:440px;background:linear-gradient(180deg,#2a2c2a,#3e423b 50%,#222)}
.we-are h2{top:108px;font-size:28px;font-weight:400;color:var(--white)}
.we-are p{left:190px;width:820px;top:170px;font-size:12px;line-height:18px;color:#dcdcdc}
.we-are .btn{left:544px;top:236px;width:112px;background:var(--white);color:var(--ink)}

/* services */
.services{height:792px;background:var(--black);color:var(--white)}
.services h2{top:104px;font-size:30px;font-weight:400}
.services p{left:220px;width:760px;top:180px;font-size:12px;line-height:18px;color:#cfcfcf}
.service{position:absolute;top:334px;width:260px;text-align:center}
.service .circle{width:216px;height:216px;border-radius:50%;border:5px solid var(--white);margin:0 auto}
.service span{display:block;margin-top:44px;font-size:15px;font-weight:600}
.services .btn{left:540px;top:690px;width:120px;background:#555}

/* apply */
.apply{height:568px}
.apply h2{top:92px;font-size:32px;font-weight:400}
.apply p{left:200px;width:800px;top:152px;font-size:12px;line-height:18px;color:#666}
.apply h3{top:246px;font-size:24px;font-weight:400}
.field{position:absolute;height:32px;background:var(--light);border:1px solid var(--line);font-size:12px;color:var(--grey);padding:8px 10px}
.apply .btn{left:540px;top:420px;width:120px}

/* contact */
.contact{height:760px;background:var(--black)}
.contact h2{top:104px;font-size:30px;font-weight:400;color:var(--white)}
.form-box{left:228px;top:212px;width:744px;height:416px;background:var(--white)}
.form-box label{position:absolute;font-size:12px;color:#555}
.form-box .btn{left:312px;top:368px;width:120px}

/* testimonials */
.testimonials{height:520px}
.testimonials h2{top:168px;font-size:32px;font-weight:400}
.avatar{position:absolute;width:76px;height:76px;border-radius:50%;background:linear-gradient(160deg,#d8c2ae,#8e7968)}
.quote{position:absolute;top:260px;width:380px;height:136px;border:1px solid #e4e4e4;background:var(--white);padding:18px 22px;font-size:12px;line-height:18px;color:#666}
.quote b{display:block;margin-top:8px;color:var(--accent);font-weight:600}

/* footer */
.site-footer{height:300px;background:var(--black);color:var(--white);text-align:center}
.site-footer .addr{top:92px;font-size:14px}
.site-footer .phone{top:118px;font-size:14px;font-weight:600}
.site-footer .social{position:absolute;left:0;right:0;top:184px;margin:0}
.site-footer .social i{background:var(--white)}
.copy{height:32px;background:var(--foot-bar);color:#bbb;font-size:11px;line-height:32px;text-align:center}
</style>
</head>
<body>

<header class="site-header">
  <div class="abs logo">VORLEN</div>
  <div class="abs contact-item" style="left:510px;width:140px"><small>Call us</small><strong>1-888-555-0142</strong></div>
  <div class="abs contact-item" style="left:740px;width:160px"><small>Email us</small><strong style="font-size:14px;font-weight:500">info@vorlen.example</strong></div>
  <div class="abs contact-item" style="left:960px;width:120px"><small>Follow us</small><div class="social"><i></i><i></i><i></i><i></i><i></i></div></div>
</header>

<nav class="main-nav">
  <span class="item home">Home</span>
  <span class="item" style="left:300px">About</span>
  <span class="item" style="left:520px">Services &amp; Benefits &amp; More</span>
  <div class="search">Search</div>
</nav>

<section class="hero" role="img" aria-label="Guests celebrating with champagne glasses at an evening party">
  <h1 class="abs">A Members Only Lifestyle Club</h1>
  <p class="abs">Exclusive access to private travel, curated experiences and events, arranged with care for members who expect more from every day.</p>
  <div class="btn" style="left:288px;width:90px">Join Now</div>
  <div class="btn" style="left:420px;width:90px">Learn More</div>
  <div class="abs dots"><i></i><i></i><i></i></div>
</section>

<section class="about">
  <h2 class="abs">About <b>VORLEN</b></h2>
  <h3 class="abs">The ultimate full service lifestyle club</h3>
  <p class="abs">VORLEN was founded to bring the finest services, benefits and experiences together in one membership. We work with trusted partners across travel, dining, events and wellness so every request is handled quickly and discreetly. Our members enjoy private concierge support, priority booking, exclusive rates and personal attention, all designed to save time and add more value to every part of life.</p>
  <div class="btn" style="left:84px;top:400px;width:120px">Apply</div>
  <div class="abs about-photo" role="img" aria-label="Portrait of a man in a suit and sunglasses beside a car"></div>
</section>

<section class="we-are" role="img" aria-label="Members gathered at an outdoor evening event">
  <h2 class="abs center">We Are <b>VORLEN</b></h2>
  <p class="abs" style="text-align:center">Built on the idea of a lifestyle without limits, VORLEN gives members a single place to arrange travel, events, experiences and everyday services with ease and privacy.</p>
  <div class="btn">Read More</div>
</section>

<section class="services">
  <h2 class="abs center">Services &amp; Benefits</h2>
  <p class="abs" style="text-align:center">VORLEN membership provides you with outstanding benefits and services. Members receive access to trusted advisors, private travel, premium dining, event tickets and wellness partners. Every request is handled by a personal concierge who knows your preferences and plans each detail ahead.</p>
  <div class="service" style="left:74px"><div class="circle" role="img" aria-label="Traveller beside a private jet" style="background:linear-gradient(160deg,#7fa7c9,#c9b29a 60%,#5a4a3c)"></div><span>Private Jet Travel</span></div>
  <div class="service" style="left:326px"><div class="circle" role="img" aria-label="Infinity pool at sunset" style="background:linear-gradient(180deg,#f2b8a4,#e99a86 50%,#c27a66)"></div><span>Experience</span></div>
  <div class="service" style="left:594px"><div class="circle" role="img" aria-label="Outdoor private event with tables" style="background:linear-gradient(160deg,#c6d3df,#9a8d7c 55%,#5d5244)"></div><span>Private Events</span></div>
  <div class="service" style="left:870px"><div class="circle" role="img" aria-label="Concert crowd under stage lights" style="background:linear-gradient(180deg,#b49be0,#6a4fc4 55%,#2b1f5c)"></div><span>Event Access</span></div>
  <div class="btn">More Services</div>
</section>

<section class="apply">
  <h2 class="abs center">Apply For a Lifestyle Club</h2>
  <p class="abs" style="text-align:center">Hello, thank you for your interest! We will begin accepting applications soon.<br>In the meantime, please fill out the indication of interest below and we will be in touch shortly.</p>
  <h3 class="abs center">Indication of Interest</h3>
  <div class="field" style="left:172px;top:340px;width:280px">Name</div>
  <div class="field" style="left:464px;top:340px;width:272px">Email</div>
  <div class="field" style="left:748px;top:340px;width:280px">Phone</div>
  <div class="btn">Submit</div>
</section>

<section class="contact">
  <h2 class="abs center">We're always here, drop us a line!</h2>
  <div class="abs form-box">
    <label style="left:36px;top:32px">Name</label>
    <div class="field" style="left:36px;top:52px;width:324px;height:28px"></div>
    <label style="left:384px;top:32px">Email</label>
    <div class="field" style="left:384px;top:52px;width:324px;height:28px"></div>
    <label style="left:36px;top:104px">Subject</label>
    <div class="field" style="left:36px;top:124px;width:672px;height:28px"></div>
    <label style="left:36px;top:176px">Message</label>
    <div class="field" style="left:36px;top:196px;width:672px;height:110px"></div>
    <div class="btn">Send</div>
  </div>
</section>

<section class="testimonials">
  <h2 class="abs center">Client Testimonials</h2>
  <div class="avatar" role="img" aria-label="Member portrait" style="left:156px;top:268px"></div>
  <div class="quote" style="left:248px">A single call and everything was arranged, from the flight to the dinner table. VORLEN truly changed how we travel.<b>John Mercer</b></div>
  <div class="avatar" role="img" aria-label="Member portrait" style="left:624px;top:268px"></div>
  <div class="quote" style="left:716px">The events are beautifully run and the team always remembers what we like. Worth every part of membership.<b>Anna Whitlow</b></div>
</section>

<footer class="site-footer">
  <div class="abs center addr">4120 Larkfield Row, Anchorage, Alaska 99501</div>
  <div class="abs center phone">Phone: 1-888-555-0142</div>
  <div class="social"><i></i><i></i><i></i><i></i><i></i></div>
</footer>
<div class="copy">© 2024 VORLEN. All Rights Reserved.</div>

</body>
</html>
```